Long term design collaboration - mobile app design & web app design

We are looking for a talented mobile designer to help us improve our UI & UX for mobile app and web app.

The screens that need to be redesigned are attached.

There is potentially a lot more work in future design available for the successful candidate.
The successful candidate would have to take part in daily stand-up around 3 times per week.
The successful candidate would join a dev team
We are software company that does property management

```html
<!DOCTYPE html>
<html lang="en">
<head>
<meta charset="utf-8">
<title>Halden – Property Management Screens</title>
<link href="https://fonts.googleapis.com/css2?family=Figtree:wght@400;500;600;700&display=swap" rel="stylesheet">
<style>
:root{
  --navy:#0b1628;
  --blue:#2b56d6;
  --text:#1b2333;
  --muted:#6b7280;
  --line:#e6e8ee;
  --bg:#f4f6fa;
  --card:#ffffff;
  --warn:#f5a623;
  --warn-bg:#fdf6e9;
  --warn-line:#f3c97a;
  --danger:#e5262b;
  --ok-bg:#e3f6e6;
  --ok:#2f9e48;
  --avatar:#b3398c;
}
*{box-sizing:border-box;margin:0;padding:0}
html,body{width:1200px;height:466px;overflow:hidden;background:#fff}
body{font-family:'Figtree',sans-serif;color:var(--text)}
.stage{position:absolute;left:0;top:0;width:2576px;height:1000px;transform:scale(.46584);transform-origin:0 0}
.screen{position:absolute;overflow:hidden;background:var(--bg);border-radius:12px}
.desk-1{left:42px;top:42px;width:750px;height:916px}
.desk-2{left:834px;top:42px;width:751px;height:468px}
.phone{top:42px;width:195px;height:423px;border-radius:22px}
.phone-1{left:1627px}.phone-2{left:1864px}.phone-3{left:2101px}.phone-4{left:2338px;background:var(--navy)}

.sidebar{position:absolute;left:0;top:0;bottom:0;width:156px;background:var(--navy);color:#fff}
.brand{position:absolute;left:11px;top:9px;font-size:16px;line-height:20px;font-weight:600;letter-spacing:5px;color:#fff}
.nav{position:absolute;left:0;right:0;top:38px}
.nav-item{height:27.1px;display:flex;align-items:center;gap:9px;padding-left:11px;font-size:8px;font-weight:500;color:#fff;white-space:nowrap}
.nav-item.active{background:var(--blue)}
.nav-item svg{width:9px;height:9px;flex:none}

.main{position:absolute;left:156px;right:0;top:0;bottom:0}
.topbar{position:absolute;right:20px;top:8px;height:20px;display:flex;align-items:center}
.bell{width:11px;height:11px;margin-right:15px;overflow:visible}
.avatar{width:20px;height:20px;border-radius:50%;background:var(--avatar);color:#fff;font-size:6.5px;font-weight:600;display:flex;align-items:center;justify-content:center;margin-right:7px}
.user{line-height:1.15;margin-right:20px}
.user b{display:block;font-size:8px;font-weight:600}
.user span{font-size:6.5px;color:var(--muted)}
.page-title{position:absolute;left:21px;top:47px;font-size:15px;line-height:20px;font-weight:600}
.btn{display:flex;align-items:center;justify-content:center;border-radius:3px;font-size:7.5px;font-weight:600}
.btn-primary{background:var(--blue);color:#fff}
.report{position:absolute;left:529px;top:46px;width:44px;height:22px}

.setup{position:absolute;left:21px;top:85px;width:552px;height:100px;background:var(--warn-bg);border:1.5px solid var(--warn-line);border-radius:5px}
.setup-title{position:absolute;left:11px;top:10px;display:flex;gap:7px;align-items:center;font-size:8px;font-weight:600}
.setup-grid{position:absolute;left:11px;top:32px;display:grid;grid-template-columns:259px 262px;gap:4px 6px}
.setup-cell{height:25px;background:#fff;display:flex;align-items:center;justify-content:space-between;padding:0 10px;font-size:7.5px;font-weight:600}

.tabs{position:absolute;left:214px;top:201px;width:166px;height:27px;border:1px solid var(--line);border-radius:3px;background:#fff;display:flex}
.tab{flex:1;display:flex;align-items:center;justify-content:center;gap:7px;font-size:7.5px;color:var(--muted)}
.tab.active{color:var(--text);font-weight:600;border-bottom:2px solid var(--blue)}

.sections{position:absolute;left:21px;top:246px;width:552px;display:flex;flex-direction:column;gap:9px}
.card{background:var(--card);border:1px solid var(--line);border-radius:3px;padding:0 12px}
.card-title{height:30px;display:flex;align-items:center;font-size:11px;font-weight:600}
.row{height:27.6px;border-top:1px solid var(--line);display:grid;grid-template-columns:19px 167px 1fr 8px;align-items:center;font-size:7.5px}
.row .label{font-weight:600}
.row .value{color:var(--muted)}
.dot{width:7px;height:7px;border-radius:50%}
.dot.warn{background:var(--warn)}.dot.danger{background:var(--danger)}
.chev{width:7px;height:7px}

.back{position:absolute;left:21px;top:12px;display:flex;gap:8px;align-items:center;font-size:7.5px;color:var(--blue)}
.back svg{width:11px;height:11px}
.list{position:absolute;left:21px;right:21px;top:85px;display:flex;flex-direction:column;gap:9px}
.list-item{height:39px;background:#fff;border:1px solid var(--line);border-radius:3px;display:flex;align-items:center;padding:0 12px;gap:10px}
.list-item .txt{flex:1;line-height:1.35}
.list-item b{display:block;font-size:8px;font-weight:600}
.list-item span{font-size:6px;color:var(--muted)}
.pill{background:var(--ok-bg);color:var(--ok);font-size:6.5px;padding:3px 7px;border-radius:8px}

.status{position:absolute;left:0;right:0;top:6px;height:10px;padding:0 14px 0 16px;display:flex;justify-content:space-between;align-items:center;font-size:7px;font-weight:600}
.status-icons{display:flex;gap:2px;align-items:center}
.status-icons i{display:block;background:currentColor;border-radius:1px}
.phone-bar{position:absolute;left:10px;right:10px;top:31px;height:16px;display:flex;align-items:center}
.phone-bar .grow{flex:1}
.phone-bar .bell{margin-right:15px}
.phone-bar .avatar{width:15px;height:15px;font-size:5px;margin-right:3px}
.phone-title{position:absolute;left:10px;top:64px;font-size:14px;line-height:18px;font-weight:600;white-space:nowrap}
.m-cards{position:absolute;left:10px;right:10px;top:100px;display:flex;flex-direction:column;gap:10px}
.m-card{background:#fff;border:1px solid var(--line);border-radius:3px;padding:0 10px}
.m-title{height:27px;display:flex;align-items:center;font-size:9px;font-weight:600}
.m-row{height:40px;border-top:1px solid var(--line);padding-left:19px;display:flex;align-items:center;font-size:7px;position:relative}
.m-row.tall{height:50px}
.m-row .txt{flex:1;line-height:1.45}
.m-row b{display:block;font-weight:600}
.m-row span{color:var(--muted)}
.m-row .dot{position:absolute;left:0;top:17px}
.fin-head{height:23px;display:flex;justify-content:space-between;align-items:center;font-size:7px;font-weight:600;border-top:1px solid var(--line)}
.fin-line{display:grid;grid-template-columns:22px 52px 1fr;align-items:center;font-size:7px;height:21px}
.fin-line span{color:var(--muted)}
.fin-line svg{width:9px;height:9px}
.fin-gap{height:6px}
.radio{display:flex;gap:9px;align-items:center;font-size:7px;line-height:1.35;min-height:30px;border-top:1px solid var(--line)}
.radio.tall{min-height:36px}
.radio i{width:9px;height:9px;border:1px solid #9aa1ae;border-radius:50%;flex:none}
.radio i.on{border:2.5px solid var(--blue)}
.m-actions{position:absolute;left:10px;right:10px;top:374px;display:flex;gap:9px}
.m-actions .btn{flex:1;height:22px;font-size:7px}
.btn-ghost{background:#fff;border:1px solid var(--line);color:var(--blue)}
.home-ind{position:absolute;left:50%;bottom:6px;width:70px;height:2.5px;margin-left:-35px;border-radius:2px;background:var(--text);z-index:2}
.phone-4 .home-ind{background:#fff}
.phone-4 .brand{left:12px;top:30px}
.close{position:absolute;right:12px;top:34px;width:10px;height:10px}
.phone-4 .nav{top:58px}
.phone-4 .nav-item{padding-left:12px}
.phone-4 .status{color:#fff}
</style>
</head>
<body>
<svg width="0" height="0" style="position:absolute">
  <defs>
    <symbol id="i-nav" viewBox="0 0 14 14"><rect x="2" y="1.5" width="10" height="11" rx="1.5" fill="none" stroke="currentColor" stroke-width="1.3"/><path d="M4.5 5h5M4.5 8h3" stroke="currentColor" stroke-width="1.2"/></symbol>
    <symbol id="i-chev" viewBox="0 0 8 8"><path d="M2.5 1l3 3-3 3" fill="none" stroke="#2b56d6" stroke-width="1.2"/></symbol>
    <symbol id="i-bell" viewBox="0 0 14 14"><path d="M3 10V6.5a4 4 0 018 0V10l1 1.2H2z M5.8 12.3h2.4" fill="none" stroke="#1b2333" stroke-width="1.1"/><circle cx="12" cy="2" r="1.8" fill="#2b56d6"/></symbol>
    <symbol id="i-out" viewBox="0 0 14 14"><path d="M8 2H3v10h5M6 7h6M10 5l2 2-2 2" fill="none" stroke="#1b2333" stroke-width="1.1"/></symbol>
    <symbol id="i-back" viewBox="0 0 14 14"><path d="M12 7H2M6 3L2 7l4 4" fill="none" stroke="currentColor" stroke-width="1.2"/></symbol>
    <symbol id="i-doc" viewBox="0 0 10 10"><rect x="1.5" y="1" width="7" height="8" rx="1" fill="none" stroke="#9aa1ae" stroke-width=".9"/><path d="M3 4h4M3 6h3" stroke="#9aa1ae" stroke-width=".8"/></symbol>
  </defs>
</svg>

<div class="stage">

  <!-- Desktop: Overview -->
  <section class="screen desk-1">
    <aside class="sidebar">
      <div class="brand">HALDEN</div>
      <nav class="nav">
        <div class="nav-item"><svg><use href="#i-nav"/></svg>User Directory</div>
        <div class="nav-item"><svg><use href="#i-nav"/></svg>Switch Development</div>
        <div class="nav-item active"><svg><use href="#i-nav"/></svg>Service Charge</div>
        <div class="nav-item"><svg><use href="#i-nav"/></svg>Property Balance</div>
        <div class="nav-item"><svg><use href="#i-nav"/></svg>Sending Letter</div>
        <div class="nav-item"><svg><use href="#i-nav"/></svg>Regular Services</div>
      </nav>
    </aside>
    <main class="main">
      <div class="topbar">
        <svg class="bell"><use href="#i-bell"/></svg>
        <div class="avatar">CW</div>
        <div class="user"><b>Clara Whitfield</b><span>Development Manager</span></div>
        <svg width="11" height="11"><use href="#i-out"/></svg>
      </div>
      <h1 class="page-title">Overview</h1>
      <div class="btn btn-primary report">Report</div>

      <div class="setup">
        <div class="setup-title"><svg width="10" height="10" viewBox="0 0 13 13"><circle cx="6.5" cy="6.5" r="5.5" fill="none" stroke="#e5262b" stroke-width="1.2"/><path d="M6.5 3.5v3.5M6.5 8.8v.8" stroke="#e5262b" stroke-width="1.2"/></svg>Please complete basic setups</div>
        <div class="setup-grid">
          <div class="setup-cell">Service Charge Schedules<svg class="chev"><use href="#i-chev"/></svg></div>
          <div class="setup-cell">Invite Residents &amp; Leaseholders<svg class="chev"><use href="#i-chev"/></svg></div>
          <div class="setup-cell">Service Charge Appointment<svg class="chev"><use href="#i-chev"/></svg></div>
          <div class="setup-cell">Connect Payment Provider<svg class="chev"><use href="#i-chev"/></svg></div>
        </div>
      </div>

      <div class="tabs">
        <div class="tab active"><svg width="10" height="10"><use href="#i-nav"/></svg>Summary</div>
        <div class="tab"><svg width="10" height="10"><use href="#i-nav"/></svg>Details</div>
      </div>

      <div class="sections">
        <div class="card">
          <div class="card-title">General</div>
          <div class="row"><i></i><span class="label">Units</span><span class="value">85</span><svg class="chev"><use href="#i-chev"/></svg></div>
          <div class="row"><i></i><span class="label">Handover Date</span><span class="value">12 January 2023</span><svg class="chev"><use href="#i-chev"/></svg></div>
          <div class="row"><i></i><span class="label">Address</span><span class="value">24 Marsh Lane, Leeds, LS2 7HQ</span><svg class="chev"><use href="#i-chev"/></svg></div>
          <div class="row"><i></i><span class="label">Section 20 Limit</span><span class="value">£20</span><i></i></div>
        </div>
        <div class="card">
          <div class="card-title">Compliance</div>
          <div class="row"><i></i><span class="label">Asbestos</span><span class="value">NA</span><svg class="chev"><use href="#i-chev"/></svg></div>
          <div class="row"><i class="dot warn"></i><span class="label">Legionellas</span><span class="value">-</span><svg class="chev"><use href="#i-chev"/></svg></div>
          <div class="row"><i class="dot danger"></i><span class="label">Drains</span><span class="value">Overdue 10 December 2023</span><svg class="chev"><use href="#i-chev"/></svg></div>
          <div class="row"><i></i><span class="label">Gutters</span><span class="value">NA</span><svg class="chev"><use href="#i-chev"/></svg></div>
          <div class="row"><i></i><span class="label">Dry Risers</span><span class="value">NA</span><svg class="chev"><use href="#i-chev"/></svg></div>
        </div>
        <div class="card">
          <div class="card-title">Insurances</div>
          <div class="row"><i></i><span class="label">Terrorism</span><span class="value">NA</span><svg class="chev"><use href="#i-chev"/></svg></div>
          <div class="row"><i></i><span class="label">Buildings</span><span class="value">NA</span><svg class="chev"><use href="#i-chev"/></svg></div>
          <div class="row"><i></i><span class="label">Engineering</span><span class="value">NA</span><svg class="chev"><use href="#i-chev"/></svg></div>
          <div class="row"><i></i><span class="label">D &amp; O</span><span class="value">NA</span><svg class="chev"><use href="#i-chev"/></svg></div>
          <div class="row"><i></i><span class="label">Reinstatement</span><span class="value">NA</span><svg class="chev"><use href="#i-chev"/></svg></div>
        </div>
        <div class="card">
          <div class="card-title">Service Charge</div>
          <div class="row"><i></i><span class="label">Year End</span><span class="value">12 December 2024</span><svg class="chev"><use href="#i-chev"/></svg></div>
          <div class="row"><i></i><span class="label">Demand Dates</span><span class="value">NA</span><svg class="chev"><use href="#i-chev"/></svg></div>
        </div>
        <div class="card">
          <div class="card-title">Cosec</div>
          <div class="row"><i></i><span class="label">Are we responsible?</span><span class="value">No</span><svg class="chev"><use href="#i-chev"/></svg></div>
        </div>
      </div>
    </main>
  </section>

  <!-- Desktop: Finances -->
  <section class="screen desk-2">
    <aside class="sidebar">
      <div class="brand">HALDEN</div>
      <nav class="nav">
        <div class="nav-item"><svg><use href="#i-nav"/></svg>Home</div>
        <div class="nav-item"><svg><use href="#i-nav"/></svg>Announcements</div>
        <div class="nav-item"><svg><use href="#i-nav"/></svg>Bank Balance</div>
        <div class="nav-item"><svg><use href="#i-nav"/></svg>Billing</div>
        <div class="nav-item active"><svg><use href="#i-nav"/></svg>Development Parameters</div>
        <div class="nav-item"><svg><use href="#i-nav"/></svg>Directory</div>
        <div class="nav-item"><svg><use href="#i-nav"/></svg>Documents</div>
        <div class="nav-item"><svg><use href="#i-nav"/></svg>Ground Rent</div>
        <div class="nav-item"><svg><use href="#i-nav"/></svg>Notifications</div>
        <div class="nav-item"><svg><use href="#i-nav"/></svg>Messages</div>
        <div class="nav-item"><svg><use href="#i-nav"/></svg>Packages</div>
        <div class="nav-item"><svg><use href="#i-nav"/></svg>Property Balance</div>
        <div class="nav-item"><svg><use href="#i-nav"/></svg>Service Charge</div>
        <div class="nav-item"><svg><use href="#i-nav"/></svg>Settings</div>
        <div class="nav-item"><svg><use href="#i-nav"/></svg>Tickets</div>
      </nav>
    </aside>
    <main class="main">
      <div class="back"><svg><use href="#i-back"/></svg>Back</div>
      <div class="topbar">
        <svg class="bell"><use href="#i-bell"/></svg>
        <div class="avatar">CW</div>
        <div class="user"><b>Clara Whitfield</b><span>Development Manager</span></div>
        <svg width="11" height="11"><use href="#i-out"/></svg>
      </div>
      <h1 class="page-title">Finances</h1>
      <div class="list">
        <div class="list-item"><div class="txt"><b>Sub-Account</b><span>Short description lorem ipsum dolor sitamet</span></div><svg class="chev"><use href="#i-chev"/></svg></div>
        <div class="list-item"><div class="txt"><b>Payment Provider</b><span>Short description lorem ipsum dolor sitamet</span></div><span class="pill">Connected</span><svg class="chev"><use href="#i-chev"/></svg></div>
      </div>
    </main>
  </section>

  <!-- Mobile: Development Overview -->
  <section class="screen phone phone-1">
    <div class="status"><span>9:41</span><span class="status-icons"><i style="width:6px;height:4px"></i><i style="width:5px;height:4px"></i><i style="width:9px;height:4px"></i></span></div>
    <div class="phone-bar">
      <svg width="10" height="8" viewBox="0 0 11 9"><path d="M0 1h11M0 4.5h11M0 8h11" stroke="#6b7280" stroke-width="1"/></svg>
      <span class="grow"></span>
      <svg class="bell"><use href="#i-bell"/></svg>
      <div class="avatar">CW</div>
    </div>
    <h1 class="phone-title">Development Overview</h1>
    <div class="m-cards">
      <div class="m-card">
        <div class="m-title">General</div>
        <div class="m-row"><div class="txt"><b>Handover Date</b><span>12 January 2023</span></div><svg class="chev"><use href="#i-chev"/></svg></div>
        <div class="m-row"><div class="txt"><b>Units</b><span>85</span></div><svg class="chev"><use href="#i-chev"/></svg></div>
        <div class="m-row tall"><div class="txt"><b>Address</b><span>24 Marsh Lane,<br>Leeds, LS2 7HQ</span></div><svg class="chev"><use href="#i-chev"/></svg></div>
        <div class="m-row"><div class="txt"><b>Section 20 Limit</b><span>£20</span></div><svg class="chev"><use href="#i-chev"/></svg></div>
      </div>
      <div class="m-card">
        <div class="m-title">Compliances</div>
        <div class="m-row"><div class="txt"><b>Asbestos</b><span>NA</span></div><svg class="chev"><use href="#i-chev"/></svg></div>
        <div class="m-row"><i class="dot warn"></i><div class="txt"><b>EICR</b><span>-</span></div><svg class="chev"><use href="#i-chev"/></svg></div>
      </div>
    </div>
    <div class="home-ind"></div>
  </section>

  <!-- Mobile: Finance -->
  <section class="screen phone phone-2">
    <div class="status"><span>9:41</span><span class="status-icons"><i style="width:6px;height:4px"></i><i style="width:5px;height:4px"></i><i style="width:9px;height:4px"></i></span></div>
    <div class="phone-bar">
      <svg width="11" height="11" style="color:#6b7280"><use href="#i-back"/></svg>
      <span class="grow"></span>
      <svg class="bell"><use href="#i-bell"/></svg>
      <div class="avatar">CW</div>
    </div>
    <h1 class="phone-title">Finance</h1>
    <div class="m-cards">
      <div class="m-card">
        <div class="m-title">Accounts Receivable</div>
        <div class="fin-head">Arrears<svg class="chev"><use href="#i-chev"/></svg></div>
        <div class="fin-line"><svg><use href="#i-doc"/></svg><span>Total</span>£7,268.22</div>
        <div class="fin-line"><svg><use href="#i-doc"/></svg><span>Bills</span>5</div>
        <div class="fin-gap"></div>
        <div class="fin-head">Unallocated Receipts<svg class="chev"><use href="#i-chev"/></svg></div>
        <div class="fin-line"><svg><use href="#i-doc"/></svg><span>Total</span>£7,268.22</div>
        <div class="fin-line"><svg><use href="#i-doc"/></svg><span>Receipts</span>5</div>
      </div>
      <div class="m-card">
        <div class="m-title">Accounts Payable</div>
        <div class="fin-head">Invoices<svg class="chev"><use href="#i-chev"/></svg></div>
        <div class="fin-line"><svg><use href="#i-doc"/></svg><span>Total</span>£4,268.78</div>
        <div class="fin-line"><svg><use href="#i-doc"/></svg><span>Bills</span>5</div>
      </div>
    </div>
    <div class="home-ind"></div>
  </section>

  <!-- Mobile: Legionellas -->
  <section class="screen phone phone-3">
    <div class="status"><span>9:41</span><span class="status-icons"><i style="width:6px;height:4px"></i><i style="width:5px;height:4px"></i><i style="width:9px;height:4px"></i></span></div>
    <div class="phone-bar">
      <svg width="11" height="11" style="color:#6b7280"><use href="#i-back"/></svg>
      <span class="grow"></span>
      <svg class="bell"><use href="#i-bell"/></svg>
      <div class="avatar">CW</div>
    </div>
    <h1 class="phone-title">Legionellas</h1>
    <div class="m-cards">
      <div class="m-card">
        <div class="m-title" style="font-size:7.5px">Is it required?</div>
        <div class="radio"><i></i>No</div>
        <div class="radio tall"><i></i>Yes, but I don't have a file to<br>upload</div>
        <div class="radio"><i class="on"></i>Yes, and I have a file to upload</div>
      </div>
    </div>
    <div class="m-actions">
      <div class="btn btn-ghost">Previous</div>
      <div class="btn btn-primary">Next</div>
    </div>
    <div class="home-ind"></div>
  </section>

  <!-- Mobile: Menu -->
  <section class="screen phone phone-4">
    <div class="status"><span>9:41</span><span class="status-icons"><i style="width:6px;height:4px"></i><i style="width:5px;height:4px"></i><i style="width:9px;height:4px"></i></span></div>
    <div class="brand">HALDEN</div>
    <svg class="close" viewBox="0 0 12 12"><path d="M1 1l10 10M11 1L1 11" stroke="#fff" stroke-width="1.3"/></svg>
    <nav class="nav">
      <div class="nav-item"><svg><use href="#i-nav"/></svg>Home</div>
      <div class="nav-item"><svg><use href="#i-nav"/></svg>Announcements</div>
      <div class="nav-item"><svg><use href="#i-nav"/></svg>Bank Balance</div>
      <div class="nav-item"><svg><use href="#i-nav"/></svg>Billing</div>
      <div class="nav-item active"><svg><use href="#i-nav"/></svg>Development Parameters</div>
      <div class="nav-item"><svg><use href="#i-nav"/></svg>Directory</div>
      <div class="nav-item"><svg><use href="#i-nav"/></svg>Documents</div>
      <div class="nav-item"><svg><use href="#i-nav"/></svg>Ground Rent</div>
      <div class="nav-item"><svg><use href="#i-nav"/></svg>Notifications</div>
      <div class="nav-item"><svg><use href="#i-nav"/></svg>Messages</div>
      <div class="nav-item"><svg><use href="#i-nav"/></svg>Packages</div>
      <div class="nav-item"><svg><use href="#i-nav"/></svg>Property Balance</div>
      <div class="nav-item"><svg><use href="#i-nav"/></svg>Service Charge</div>
      <div class="nav-item"><svg><use href="#i-nav"/></svg>Settings</div>
    </nav>
    <div class="home-ind"></div>
  </section>

</div>
</body>
</html>
```